Report template for evaluation reports to be used by non designers

We are looking for a report template that meets all the requirements listed in the attached documents. letter head, logo etc have been enclosed. Its important that the colour integrity is kept, but beyond that options are welcome.
Its important that the document is extremely easy to use and that is able to be adapted to include eatables, figures, pictures, text boxes etc and keep the integrity of the template

Target Market(s)

Governments, Civil society organisations and research institutions

Font styles to use
Sans Serif

Colors
6b449b
876aae
c0c0c0
000000

Requirements
Must have
• Clean, professional, not concluded, modern, must be easy to use
Should not have
• too busy, hard to use

```html
<!DOCTYPE html>
<html lang="en">
<head>
<meta charset="utf-8">
<title>Civic Insight Institute – Report Cover</title>
<link href="https://fonts.googleapis.com/css2?family=Montserrat:wght@400;500;700&family=Oswald:wght@700&display=swap" rel="stylesheet">
<style>
  :root {
    --purple: #6b449b;
    --lilac: #876aae;
    --silver: #c0c0c0;
    --ink: #000000;
    --paper: #ffffff;
    --backdrop: #e4e4e6;
    --muted: #555555;
  }
  * { box-sizing: border-box; margin: 0; padding: 0; }
  html, body { width: 1200px; height: 847px; overflow: hidden; background: var(--backdrop); }
  body { font-family: "Montserrat", sans-serif; color: var(--ink); }
  .spread { display: flex; width: 1200px; height: 847px; }
  .page {
    position: relative; width: 600px; height: 847px; background: var(--paper);
    border-bottom: 10px solid var(--purple); overflow: hidden;
  }
  .page--back { border-right: 1px solid #ececec; }

  /* shared brand name block */
  .brand { position: absolute; left: 0; right: 0; text-align: center; font-weight: 500; color: var(--ink); }
  .brand__name { font-size: 34px; letter-spacing: 6px; line-height: 1; }
  .brand__sub { font-size: 11px; letter-spacing: 5px; margin-top: 10px; line-height: 1; }

  /* back cover */
  .location-map {
    position: absolute; left: 30px; top: 190px; width: 540px; height: 300px;
    border: 3px solid var(--purple); border-radius: 24px;
    background: linear-gradient(135deg, #efe9dc 0%, #e8e2d3 45%, #d6e6c8 60%, #a9c8ee 80%, #efe9dc 100%);
  }
  .page--back .brand { top: 604px; }
  .page--back .brand__name { font-size: 28px; letter-spacing: 5px; }
  .contact-badge {
    position: absolute; left: 270px; top: 690px; width: 60px; height: 60px; border-radius: 50%;
    background: var(--lilac);
  }
  .contact-lines {
    position: absolute; left: 0; right: 0; top: 768px; text-align: center;
    font-size: 11px; line-height: 17px; color: var(--muted);
  }

  /* front cover */
  .report-title {
    position: absolute; left: 40px; top: 40px; display: flex; align-items: center; gap: 14px;
    font-family: "Oswald", sans-serif; font-weight: 700; font-size: 30px; line-height: 1; color: var(--purple);
  }
  .cover-visual { position: absolute; left: 180px; top: 80px; width: 420px; height: 420px; }
  .cover-visual__photo {
    position: absolute; left: 70px; top: 40px; width: 380px; height: 330px; border-radius: 50%;
    background: linear-gradient(160deg, #b9d3ea 0%, #d5e2ec 40%, #6f7782 75%, #3e434b 100%);
  }
  .cover-visual__label {
    position: absolute; left: 170px; top: 150px; font-weight: 700; font-size: 46px; line-height: 1; color: var(--paper);
  }
  .page--front .brand { top: 552px; }
  .page--front .brand__name { font-size: 40px; letter-spacing: 8px; }
  .meta-box {
    position: absolute; left: 130px; top: 680px; width: 400px; height: 72px;
    border: 2px solid var(--lilac); border-radius: 18px; padding: 12px 18px;
    font-size: 11px; font-weight: 700; color: var(--purple);
  }
  .meta-box__row { display: flex; align-items: flex-end; gap: 6px; height: 22px; }
  .meta-box__line { flex: 1; border-bottom: 1px solid var(--silver); margin-bottom: 3px; }
</style>
</head>
<body>
<main class="spread">
  <section class="page page--back">
    <div class="location-map" role="img" aria-label="Street map of the institute's location"></div>
    <div class="brand">
      <div class="brand__name">CIVIC INSIGHT</div>
      <div class="brand__sub">INSTITUTE</div>
    </div>
    <div class="contact-badge" aria-hidden="true"></div>
    <div class="contact-lines">
      info@civicinsightinstitute.org<br>www.civicinsightinstitute.org
    </div>
  </section>

  <section class="page page--front">
    <h1 class="report-title">
      <svg width="34" height="26" viewBox="0 0 34 26" aria-hidden="true">
        <polygon points="0,0 34,20 0,26" fill="#6b449b"/>
        <polygon points="0,0 34,20 8,18" fill="#876aae"/>
      </svg>
      Report Name
    </h1>

    <div class="cover-visual">
      <svg width="420" height="420" viewBox="0 0 420 420" aria-hidden="true">
        <defs>
          <linearGradient id="ringGrad" x1="0" y1="0" x2="1" y2="1">
            <stop offset="0" stop-color="#876aae"/>
            <stop offset="1" stop-color="#6b449b"/>
          </linearGradient>
        </defs>
        <ellipse cx="250" cy="210" rx="215" ry="190" fill="url(#ringGrad)"/>
        <ellipse cx="262" cy="205" rx="200" ry="176" fill="#ffffff"/>
        <path d="M250 18 C320 12 390 30 420 60 L420 85 C380 52 320 35 250 18 Z" fill="#876aae" opacity="0.7"/>
        <path d="M420 300 C380 360 300 392 200 398 C300 404 380 378 420 345 Z" fill="#876aae" opacity="0.8"/>
      </svg>
      <div class="cover-visual__photo" role="img" aria-label="Cover photograph of city towers against the sky"></div>
      <div class="cover-visual__label">Image</div>
    </div>

    <div class="brand">
      <div class="brand__name">CIVIC INSIGHT</div>
      <div class="brand__sub">INSTITUTE</div>
    </div>

    <div class="meta-box">
      <div class="meta-box__row"><span>Authors :</span><span class="meta-box__line"></span></div>
      <div class="meta-box__row"><span>Client :</span><span class="meta-box__line"></span></div>
    </div>
  </section>
</main>
</body>
</html>
```